Design for Training Manuals

We need a graphic design for new training manuals for our organization called Lanternfield Trust, Inc. We are a children's rights NGO based in the Philippines. We are running an advocacy campaign called Raise Every Hand which advocates for the prevention of child sexual abuse and sexual exploitation of children. The Raise Every Hand Campaign is gaining momentum in various countries around the world and we would like to provide our constituents with inspiring training materials that will enable them to carry out the work of protecting children's rights.
Because of the sensitive nature of the subject matter, we would like to present a non-threatening light design, with a creative edge, that incorporates our Raise Every Hand logo. Also, I have attached an image from which you can design from.
Please feel free to visit our website for inspiration: www.lanternfieldtrust.org
Updates
Dear Designers,
I am excited about this project. I have uploaded a couple of our training modules. Overall there are 2 levels: Level 1 with 3 training modules and Level 2 also with 3 training modules.
Thank you,
Teresa
Target Market(s)
Non-government workers, government workers, teachers, social workers...
Industry/Entity Type
Graphic Design
Look and feel
Each slider illustrates characteristics of the customer's brand and the style your logo design should communicate.

```html
<!DOCTYPE html>
<html lang="en">
<head>
<meta charset="utf-8">
<title>Raise Every Hand – Training Manual, Level 1 Module I</title>
<link rel="stylesheet" href="https://fonts.googleapis.com/css2?family=EB+Garamond:wght@400;500&display=swap">
<style>
  :root {
    --page-bg: #ffffff;
    --canvas-bg: #ffffff;
    --brand-red: #9b1b1f;
    --brand-red-dark: #7d1417;
    --band-grey: #d2d3d5;
    --band-grey-light: #eeeeef;
    --text: #1d1d1d;
    --caption: #6b6b6b;
    --border: #bdbdbd;
    --tab-shadow: #c9c9c9;
  }
  * { box-sizing: border-box; margin: 0; padding: 0; }
  html, body { width: 1200px; height: 867px; overflow: hidden; background: var(--canvas-bg); }
  body { position: relative; font-family: "EB Garamond", Garamond, serif; color: var(--text); }

  /* Cover */
  .cover { position: absolute; left: 0; top: 0; width: 583px; height: 823px; background: var(--page-bg); overflow: hidden; }
  .cover-art {
    position: absolute; left: 0; top: 0; width: 583px; height: 646px;
    background: linear-gradient(160deg, #f4e9c8 0%, #e7b451 22%, #c9463b 42%, #5d8fc9 60%, #3a2a22 76%, #f1d36a 100%);
  }
  .cover-brand-band {
    position: absolute; left: 0; top: 646px; width: 583px; height: 97px;
    background: linear-gradient(90deg, var(--band-grey) 0%, var(--band-grey-light) 50%, var(--band-grey) 100%);
  }
  .brand-lockup {
    position: absolute; left: 198px; top: 11px; width: 180px; height: 79px;
    background: #fff; display: flex; flex-direction: column; align-items: center; justify-content: center; gap: 4px;
  }
  .brand-name { display: flex; align-items: center; gap: 6px; font-size: 21px; font-weight: 500; color: var(--brand-red); }
  .brand-name .dot { width: 10px; height: 10px; border-radius: 50%; background: var(--brand-red); }
  .brand-tagline { font-size: 9px; color: #333; }
  .module-band {
    position: absolute; left: 0; top: 743px; width: 583px; height: 28px;
    background: var(--brand-red); color: #fff; font-size: 14px;
    display: flex; align-items: center; justify-content: center;
  }
  .cover-art-strip {
    position: absolute; left: 0; top: 771px; width: 583px; height: 52px;
    background: linear-gradient(90deg, #e9d7a6, #6a9bd1, #e7b451, #d25a4a, #f4e9c8);
  }

  /* Inside page */
  .inside { position: absolute; left: 617px; top: 0; width: 582px; height: 823px; background: var(--page-bg); border: 1px solid var(--border); }
  .running-tab {
    position: absolute; right: 21px; top: 0; width: 254px; height: 28px;
    background: var(--brand-red); color: #fff; font-size: 14px;
    display: flex; align-items: center; justify-content: center;
    box-shadow: 0 3px 0 var(--tab-shadow);
  }
  .inside-content { position: absolute; left: 32px; top: 96px; width: 510px; font-size: 10.5px; line-height: 15px; }
  .section-head {
    display: inline-block; font-size: 15px; line-height: 18px; padding-right: 24px;
    background: linear-gradient(90deg, #e2e2e2 0%, #d4d4d4 75%, #ffffff 100%);
  }
  .section { margin-bottom: 14px; }
  .topic-title { font-size: 15px; line-height: 20px; }
  .sub-head { font-size: 12px; margin-top: 14px; }
  ol, ul { list-style: none; }
  .num-list li, .bullet-list li { display: flex; }
  .num-list li span:first-child, .bullet-list li span:first-child { width: 35px; flex: none; }
  .process-head { margin-top: 10px; font-size: 12px; line-height: 17px; padding-right: 18px; }

  .caption { position: absolute; top: 836px; font-size: 22px; color: var(--caption); transform: translateX(-50%); white-space: nowrap; }
  .caption-cover { left: 291px; }
  .caption-inside { left: 937px; }
</style>
</head>
<body>

<section class="cover">
  <div class="cover-art" role="img" aria-label="Colourful illustration of a crowd of children seen from behind, surrounded by hand-lettered children's rights phrases"></div>
  <div class="cover-brand-band">
    <div class="brand-lockup">
      <div class="brand-name"><span class="dot"></span>Raise Every Hand</div>
      <div class="brand-tagline">Stop child sexual abuse and exploitation</div>
    </div>
  </div>
  <div class="module-band">Level 1 | Module I | Gender Sensitivity</div>
  <div class="cover-art-strip" role="img" aria-label="Continuation of the illustration with hand-lettered rights phrases"></div>
</section>

<section class="inside">
  <div class="running-tab">Level 1 | Module I | Gender Sensitivity</div>
  <div class="inside-content">
    <div class="section">
      <h2 class="section-head">A. Objectives:</h2>
      <p>By the end of the module, the participants should be able to:</p>
      <ol class="num-list">
        <li><span>1.</span><span>Differentiate the concepts of Gender and Sex.</span></li>
        <li><span>2.</span><span>Identify the different Gender Issues and how they are perpetrated.</span></li>
        <li><span>3.</span><span>Understand the concept of power relations.</span></li>
        <li><span>4.</span><span>Relate Gender Issues to Child Sexual Abuse and Exploitation issues.</span></li>
      </ol>
    </div>
    <div class="section">
      <h2 class="section-head">B. Duration:</h2>
      <p>1 day</p>
    </div>
    <div class="section">
      <h2 class="section-head">C. Session Flow:</h2>
      <h3 class="topic-title">Topic 1: The concept of Inequality</h3>
      <h4 class="sub-head">Things to prepare:</h4>
      <p>A list of statements written in Manila paper or prepared in powerpoint.</p>
      <p>Statements:</p>
      <p>“It is alright for my daughter to marry a member of an Indigenous tribe.”</p>
      <p>“It would be a problem if the President of our country would be a deaf person.”</p>
      <p>“A good looking politician has more chance of winning than an ugly one.”</p>
      <p>“Midgets shouldn’t be allowed to work for the police.”</p>
      <p>“When a child and an adult has different opinions, most often, the opinion of the adult is the right one.”</p>
      <p>“ If a woman likes to go out nightly and party, then that woman is a flirt.”</p>

      <h4 class="section-head process-head">Process:</h4>
      <p>Ask the participants to stand, you would read out each statement one by one, and if they agree to the statement, they will walk towards one part of the room you have designated, and if they don’t agree, they would walk towards another part of the room. For each statement, ask the opinions from each side, taking note to get arguments and counter-arguments.</p>

      <h4 class="section-head process-head">Key Topic Points:</h4>
      <ul class="bullet-list">
        <li><span>•</span><span>Inequality is related to power differences.</span></li>
        <li><span>•</span><span>Power differences take different forms, examples of which are listed below;</span></li>
        <li><span>•</span><span>Inequality because of age (Adults are right, children are wrong)</span></li>
        <li><span>•</span><span>Religion (the concept that one religion is right over the other)</span></li>
        <li><span>•</span><span>Physical traits (color of your skin, facial features, concept of beauty)</span></li>
        <li><span>•</span><span>Ethnicity</span></li>
        <li><span>•</span><span>Economic status (Richer folks have more rights)</span></li>
        <li><span>•</span><span>Gender (The concept that one sex is superior to the other)</span></li>
      </ul>
    </div>
  </div>
</section>

<p class="caption caption-cover">Manual Cover Page</p>
<p class="caption caption-inside">Inside Page look</p>

</body>
</html>
```